24 Super Fantastic Banners 4 campaigns

I need 4 campaigns to have banners made, 6 banner sizes each so 24 total banners. Here are the landing pages with the messaging.

http://www.examplebizdirectory.test/Sandy-UT/Pellworth-Medical-48271.html

http://www.examplebizdirectory.test/Darvell-Law-Group-48272.html

http://www.examplebizdirectory.test/Vuloran-48273.html

http://www.examplebizdirectory.test/Starqueb-com-48274.html

Need to get done asap. Much more work can be following right after. Here are the sizes

Sorry fix a typo. These sizes:

300 X 50
300x250
320 X50
216 X36
168 X 28
120 X 20

Medical

Requirements
Must have
• Must have phone number in the display for call to action

```html
<!DOCTYPE html>
<html lang="en">
<head>
<meta charset="utf-8">
<title>Pellworth Medical Banner Set</title>
<link href="https://fonts.googleapis.com/css2?family=Arimo:ital,wght@0,400;0,700;1,700&family=Tinos:ital,wght@1,700&display=swap" rel="stylesheet">
<style>
  :root {
    --navy: #1d3461;
    --blue: #1f4f8f;
    --blue-deep: #15346a;
    --blue-light: #3a6db0;
    --tick: #f2c318;
    --white: #ffffff;
    --ink: #222222;
    --muted: #6b7a90;
    --border: #c9d1dc;
    --photo-a: #c99a7c;
    --photo-b: #e8cdb8;
  }
  * { box-sizing: border-box; margin: 0; padding: 0; }
  html, body { width: 900px; height: 1200px; overflow: hidden; background: var(--white); }
  body { position: relative; font-family: "Arimo", Arial, sans-serif; color: var(--ink); }

  .banner { position: absolute; border: 2px solid var(--border); background: var(--white); overflow: hidden; }
  .size-label { position: absolute; width: 900px; text-align: center; font-size: 24px; color: var(--ink); }

  .photo { background: linear-gradient(135deg, var(--photo-b), var(--photo-a) 60%, var(--blue-light)); }

  .brand { display: flex; align-items: center; gap: 8px; color: var(--navy); font-weight: 700; white-space: nowrap; }
  .brand-mark { background: var(--navy); flex: none; }

  /* 300x250 */
  .rect { left: 210px; top: 36px; width: 453px; height: 450px; }
  .rect .phone { height: 84px; display: flex; align-items: center; justify-content: center; font-size: 58px; font-weight: 700; color: var(--navy); }
  .rect .hero { position: absolute; top: 84px; left: 0; width: 100%; height: 278px; background: linear-gradient(180deg, var(--blue-deep), var(--blue) 55%, var(--blue-light)); }
  .rect .hero .photo { position: absolute; right: 0; top: 60px; width: 200px; height: 218px; }
  .rect .headline { position: absolute; top: 14px; left: 0; width: 100%; text-align: center; font-size: 31px; font-style: italic; font-weight: 700; color: var(--white); }
  .rect .benefits { position: absolute; left: 14px; top: 74px; list-style: none; color: var(--white); font-size: 20px; font-weight: 700; line-height: 1.1; width: 225px; }
  .rect .benefits li { display: flex; gap: 8px; margin-bottom: 10px; }
  .rect .benefits small { font-size: 14px; font-weight: 400; }
  .rect .benefits svg { flex: none; margin-top: 1px; }
  .rect .footer { position: absolute; bottom: 0; left: 0; width: 100%; height: 88px; display: flex; align-items: center; padding-left: 18px; }
  .rect .brand { font-size: 20px; }
  .rect .brand-mark { width: 34px; height: 34px; }

  /* leaderboard strips */
  .strip { display: flex; }
  .strip .side { flex: none; background: var(--white); display: flex; flex-direction: column; justify-content: center; align-items: center; }
  .strip .phone { font-weight: 700; color: var(--navy); line-height: 1; white-space: nowrap; }
  .strip .message { flex: 1; min-width: 0; background: linear-gradient(180deg, var(--blue-deep), var(--blue)); display: flex; align-items: stretch; }
  .strip .headline { flex: 1; min-width: 0; align-self: center; font-family: "Tinos", Georgia, serif; font-style: italic; font-weight: 700; color: var(--white); line-height: 1.1; text-align: center; padding: 0 4px; }
  .strip .photo { flex: none; }

  .s320 { left: 195px; top: 552px; width: 483px; height: 78px; }
  .s320 .side { width: 222px; }
  .s320 .phone { font-size: 29px; margin-bottom: 6px; }
  .s320 .brand { font-size: 13px; gap: 6px; }
  .s320 .brand-mark { width: 16px; height: 16px; }
  .s320 .headline { font-size: 18px; }
  .s320 .photo { width: 90px; }

  .s300 { left: 210px; top: 705px; width: 453px; height: 75px; }
  .s300 .side { width: 222px; }
  .s300 .phone { font-size: 29px; margin-bottom: 6px; }
  .s300 .tag { font-size: 11px; color: var(--muted); }
  .s300 .headline { font-size: 17px; }
  .s300 .photo { width: 80px; }

  .s216 { left: 267px; top: 855px; width: 336px; height: 56px; }
  .s216 .side { width: 168px; }
  .s216 .phone { font-size: 21px; margin-bottom: 4px; }
  .s216 .brand { font-size: 9px; gap: 4px; }
  .s216 .brand-mark { width: 10px; height: 10px; }
  .s216 .headline { font-size: 13px; }
  .s216 .photo { width: 48px; }

  .s168 { left: 297px; top: 990px; width: 261px; height: 44px; }
  .s168 .side { width: 134px; }
  .s168 .phone { font-size: 16px; margin-bottom: 3px; }
  .s168 .brand { font-size: 7px; gap: 3px; }
  .s168 .brand-mark { width: 8px; height: 8px; }
  .s168 .headline { font-size: 10px; padding: 0 3px; }
  .s168 .photo { width: 36px; }
</style>
</head>
<body>

<section class="banner rect" aria-label="300 by 250 banner">
  <div class="phone">(555) 014-2786</div>
  <div class="hero">
    <div class="photo" role="img" aria-label="Smiling couple embracing"></div>
    <h2 class="headline">Diabetic Supplies Made Easy</h2>
    <ul class="benefits">
      <li><svg width="22" height="22" viewBox="0 0 24 24"><path d="M3 13l6 6L21 4" fill="none" stroke="var(--tick)" stroke-width="4" stroke-linecap="round" stroke-linejoin="round"/></svg><span>Save Money <small>on co-pays</small></span></li>
      <li><svg width="22" height="22" viewBox="0 0 24 24"><path d="M3 13l6 6L21 4" fill="none" stroke="var(--tick)" stroke-width="4" stroke-linecap="round" stroke-linejoin="round"/></svg><span>Save TIME <small>with free home delivery</small></span></li>
      <li><svg width="22" height="22" viewBox="0 0 24 24"><path d="M3 13l6 6L21 4" fill="none" stroke="var(--tick)" stroke-width="4" stroke-linecap="round" stroke-linejoin="round"/></svg><span>So Easy <small>we do work for you</small></span></li>
    </ul>
  </div>
  <div class="footer">
    <div class="brand"><span class="brand-mark"></span>PELLWORTH MEDICAL</div>
  </div>
</section>
<div class="size-label" style="top:500px">300X250</div>

<section class="banner strip s320" aria-label="320 by 50 banner">
  <div class="side">
    <div class="phone">(555) 014-2786</div>
    <div class="brand"><span class="brand-mark"></span>PELLWORTH MEDICAL</div>
  </div>
  <div class="message">
    <h2 class="headline">Diabetic Supplies Made Easy</h2>
    <div class="photo" role="img" aria-label="Smiling couple"></div>
  </div>
</section>
<div class="size-label" style="top:642px">320X50</div>

<section class="banner strip s300" aria-label="300 by 50 banner">
  <div class="side">
    <div class="phone">(555) 014-2786</div>
    <div class="tag">Diabetic Supplies Made Easy</div>
  </div>
  <div class="message">
    <h2 class="headline">Diabetic Supplies Made Easy</h2>
    <div class="photo" role="img" aria-label="Smiling couple"></div>
  </div>
</section>
<div class="size-label" style="top:792px">300X50</div>

<section class="banner strip s216" aria-label="216 by 36 banner">
  <div class="side">
    <div class="phone">(555) 014-2786</div>
    <div class="brand"><span class="brand-mark"></span>PELLWORTH MEDICAL</div>
  </div>
  <div class="message">
    <h2 class="headline">Diabetic Supplies Made Easy</h2>
    <div class="photo" role="img" aria-label="Smiling couple"></div>
  </div>
</section>
<div class="size-label" style="top:925px">216X36</div>

<section class="banner strip s168" aria-label="168 by 28 banner">
  <div class="side">
    <div class="phone">(555) 014-2786</div>
    <div class="brand"><span class="brand-mark"></span>PELLWORTH MEDICAL</div>
  </div>
  <div class="message">
    <h2 class="headline">Diabetic Supplies Made Easy</h2>
    <div class="photo" role="img" aria-label="Smiling couple"></div>
  </div>
</section>
<div class="size-label" style="top:1050px">168X28</div>

</body>
</html>
```